Torvane clean Business Cards

I'm looking for someone to design my business card using my company name and logo. I would like it it be clean, fresh and a little out of the box. The colors I would like used are the same two in my logo (gold and the teal blue color) I also want it to screen high end scene the company name is Torvane clean :) I'm a commercial cleaning company based out of Orange and San Diego county. Once I receive your email I will send over the file. Because the file is quote big with several options of logos. Please be an out of the box thinker and take some risk...I'm looking for someone to put themselves out there. Thanks and good luck

```html
<!DOCTYPE html>
<html lang="en">
<head>
<meta charset="utf-8">
<title>Torvane clean Business Cards</title>
<link rel="stylesheet" href="https://fonts.googleapis.com/css2?family=Michroma&family=Comfortaa:wght@300;400&family=Open+Sans:wght@400&display=swap">
<style>
  :root {
    --card-green: #36e58b;
    --band-brown: #7a4b25;
    --band-dark: #463a32;
    --ink-white: #ffffff;
    --accent-yellow: #e6f21e;
    --page: #ffffff;
  }
  * { margin: 0; padding: 0; box-sizing: border-box; }
  html, body { width: 959px; height: 1200px; overflow: hidden; background: var(--page); }
  .sheet { position: relative; width: 959px; height: 1200px; }

  .card { position: absolute; left: 23px; width: 897px; background: var(--card-green); }
  .card--front { top: 20px; height: 513px; }
  .card--back { top: 645px; height: 515px; }

  .brand-band { position: absolute; left: -1px; top: 126px; width: 898px; height: 213px; background: var(--band-brown); z-index: 0; }

  .brand {
    position: absolute; left: 0; right: 0; text-align: center; z-index: 1;
    font-family: "Michroma", sans-serif; color: var(--ink-white);
  }
  .brand__name { display: flex; align-items: center; justify-content: center; gap: 22px; text-transform: uppercase; letter-spacing: 2px; }
  .brand__mark { display: inline-block; background: var(--ink-white); }
  .brand__line { text-transform: uppercase; letter-spacing: 2px; white-space: nowrap; }

  .card--front .brand { top: 195px; }
  .card--front .brand__name { font-size: 48px; line-height: 70px; }
  .card--front .brand__mark { width: 30px; height: 30px; }
  .card--front .brand__line { font-size: 26px; line-height: 30px; margin-top: 2px; }

  .tagline {
    position: absolute; right: 82px; top: 307px; z-index: 1;
    font-family: "Open Sans", sans-serif; font-size: 20px; line-height: 28px; color: var(--ink-white);
  }

  .contact {
    position: absolute; left: 430px; top: 367px; list-style: none; z-index: 1;
    font-family: "Comfortaa", sans-serif; font-weight: 300; font-size: 21px; line-height: 30px; color: var(--ink-white);
  }

  .card--back .brand { top: 95px; }
  .card--back .brand__name { font-size: 36px; line-height: 54px; }
  .card--back .brand__mark { width: 22px; height: 22px; }
  .card--back .brand__line { font-size: 19px; line-height: 22px; margin-top: 0; }

  .services { position: absolute; left: 0; right: 0; top: 218px; }
  .services__title {
    text-align: center; font-family: "Comfortaa", sans-serif; font-weight: 400;
    font-size: 31px; color: var(--accent-yellow); line-height: 40px; padding-left: 16px;
  }
  .services__list {
    list-style: none; margin: 6px 0 0 290px;
    font-family: "Comfortaa", sans-serif; font-weight: 300; font-size: 24px; line-height: 35px; color: var(--ink-white);
  }

  .promise {
    position: absolute; left: 2px; top: 458px; width: 894px; height: 36px;
    background: var(--band-dark); color: var(--ink-white); text-align: center; padding-left: 20px;
    font-family: "Comfortaa", sans-serif; font-weight: 300; font-size: 22px; line-height: 36px;
  }
</style>
</head>
<body>
<main class="sheet">
  <section class="card card--front">
    <div class="brand-band"></div>
    <div class="brand">
      <div class="brand__name"><span>Torvane</span><span class="brand__mark"></span><span>Clean</span></div>
      <div class="brand__line">Commercial Cleaning Services</div>
    </div>
    <p class="tagline">"The Torvane Way to Clean"</p>
    <ul class="contact">
      <li>4715 Harlow Crest Ave. Brightvale</li>
      <li>CA 90412</li>
      <li>Phone : 1(800)555-0147</li>
      <li>Email : contact@torvanecleanco.com</li>
    </ul>
  </section>

  <section class="card card--back">
    <div class="brand">
      <div class="brand__name"><span>Torvane</span><span class="brand__mark"></span><span>Clean</span></div>
      <div class="brand__line">Commercial Cleaning Services</div>
    </div>
    <div class="services">
      <h2 class="services__title">Services :</h2>
      <ul class="services__list">
        <li>Construction Cleanup</li>
        <li>Power/Pressure Washing</li>
        <li>Strip and wax, Scrub &amp; Finish</li>
        <li>Carpet Cleaning, Green Cleaning</li>
        <li>Burnishing</li>
      </ul>
    </div>
    <p class="promise">Hard work &amp; dedication is our promise to you!</p>
  </section>
</main>
</body>
</html>
```